Cleaning service website design

We need a new nice web design(logo will be the same) for a new cleaning service Company:

Informations about Company and logo you can take from flyers in attachments.

This is a cleaning service Company which have simple rules and we would like to show that(in checklist form) on website:

- What we do and that we're Cleaning Green

- Why us?

- How much(our pricing is simple)

Also we would like to communicate with clients by some nice/big pictures on website and the most important thing is our phone number and short/fast Freestimate.

Also there should be some space for description about our Company.

Generally all information on main page can be short: about us, about service(what we do), last reviews, tips (for example: Tip of the week) and other can be some introduction to subpage where will be more information.

There will be few subpages like: About us, About our service, Photos(Before and after), Reviews , Tips, FAQ, Contact, Looking for a Job? - most of them will be just text so you can project just one example.

```html
<!DOCTYPE html>
<html lang="en">
<head>
<meta charset="utf-8">
<title>Tidy Nest House Cleaning</title>
<link rel="stylesheet" href="https://fonts.googleapis.com/css2?family=Questrial&family=Poppins:wght@600&display=swap">
<style>
  :root {
    --brand-blue: #1f4fa3;
    --brand-blue-dark: #12357a;
    --navy-text: #1c2a6b;
    --page-grey: #e3e3e8;
    --panel-white: #f2f2f5;
    --frame-white: #f7f7fa;
    --accent-green: #22f23a;
    --job-green: #2f9a2f;
    --nav-grey: #6e6e72;
    --body-text: #3a3a4a;
  }
  * { box-sizing: border-box; margin: 0; padding: 0; }
  html, body { width: 1200px; height: 1200px; overflow: hidden; }
  body {
    position: relative;
    background: var(--page-grey);
    font-family: "Questrial", "Century Gothic", sans-serif;
    color: var(--navy-text);
  }
  .top-band {
    position: absolute; left: 0; top: 0; width: 1200px; height: 133px;
    background: linear-gradient(180deg, var(--brand-blue) 0%, var(--brand-blue-dark) 100%);
  }
  .brand {
    position: absolute; right: 60px; top: 42px;
    display: flex; align-items: center; gap: 14px;
    font-size: 38px; color: #ffffff;
  }
  .brand-dot { width: 26px; height: 26px; border-radius: 50%; background: #ffffff; }

  .headline {
    position: absolute; left: 131px; top: 188px;
    font-size: 88px; line-height: 1; letter-spacing: 1px;
  }
  .tagline {
    position: absolute; left: 131px; top: 266px; width: 1000px;
    font-size: 38px; line-height: 34px;
  }

  .slider {
    position: absolute; left: 99px; top: 407px; width: 805px; height: 486px;
    background: var(--frame-white);
    box-shadow: 0 0 6px rgba(0,0,0,0.35);
  }
  .slide-photo {
    position: absolute; left: 58px; top: 26px; width: 684px; height: 434px;
    background: linear-gradient(180deg, #c9c6d4 0%, #6d5668 45%, #8a4a2a 75%, #5a2c16 100%);
  }
  .slider-arrow {
    position: absolute; top: 208px; width: 20px; height: 53px;
    background: var(--accent-green); border: 2px solid #ffffff;
  }
  .slider-arrow.prev { left: 16px; }
  .slider-arrow.next { right: 20px; }

  .intro-text {
    position: absolute; left: 131px; top: 913px; width: 745px;
    font-size: 11.5px; line-height: 16px; color: var(--body-text);
  }

  .estimate-tab {
    position: absolute; left: 951px; top: 351px; width: 249px; height: 49px;
    background: var(--brand-blue-dark); color: #ffffff;
    font-size: 22px; letter-spacing: 1px; padding: 11px 0 0 31px;
  }
  .estimate-tab::after {
    content: ""; position: absolute; right: 4px; top: 4px;
    width: 18px; height: 41px; background: var(--accent-green);
  }
  .info-panel {
    position: absolute; left: 951px; top: 405px; width: 249px; height: 595px;
    background: var(--panel-white); border: 1px solid #c8c8d0;
    padding: 24px 0 0 16px;
  }
  .panel-heading { font-size: 22px; letter-spacing: 1px; margin-bottom: 14px; }
  .panel-heading.second { margin-top: 36px; margin-bottom: 10px; }
  .panel-list { list-style: none; font-size: 14.5px; }
  .panel-list li { line-height: 22px; margin-bottom: 17px; }
  .visit-list li { margin-bottom: 16px; }

  .job-link {
    position: absolute; right: 19px; top: 1018px;
    font-family: "Poppins", Arial, sans-serif; font-weight: 600;
    font-size: 28px; color: var(--job-green);
  }

  .call-band {
    position: absolute; left: 0; top: 1065px; width: 1200px; height: 100px;
    background: linear-gradient(180deg, var(--brand-blue) 0%, var(--brand-blue-dark) 100%);
    color: var(--accent-green);
  }
  .call-number { position: absolute; left: 83px; top: 6px; font-size: 80px; }
  .call-prompt { position: absolute; left: 663px; top: 10px; font-size: 70px; }

  .main-nav {
    position: absolute; left: 0; top: 1165px; width: 1200px; height: 35px;
    background: var(--nav-grey);
  }
  .main-nav a {
    position: absolute; top: 0; height: 35px; line-height: 35px;
    color: #ffffff; text-decoration: none; font-size: 17px; text-align: center;
  }
  .main-nav a.current {
    background: var(--accent-green); border: 2px solid #ffffff; line-height: 31px;
  }
</style>
</head>
<body>
  <header class="top-band">
    <div class="brand"><span class="brand-dot"></span>Tidy Nest</div>
  </header>

  <h1 class="headline">WHY US?</h1>
  <p class="tagline">because we understand that there is more to life then just cleaning</p>

  <section class="slider">
    <div class="slide-photo" role="img" aria-label="Bright clean bedroom with a white bed, purple walls and polished wooden floor"></div>
    <span class="slider-arrow prev"></span>
    <span class="slider-arrow next"></span>
  </section>

  <p class="intro-text">Lorem ipsum dolor sit amet, in aecenas pharetra gravida ullamcorpe r neque. Sed hendrerit proin odio placerat ultrices adipiscing lectus ornare, ut velit nonummy.Lorem ipsum dolor sit amet, in aecenas pharetra gravida ullamcorper neque. Sed hendrerit proin odio placerat ultrices adipiscing lectus ornare, ut velit nonummy. Lorem ipsum dolor sit amet, in aecenas pharetra gravida ullamcorpe r neque. Sed hendrerit proin odio placerat ultrices adipiscing lectus ornare, ut velit nonummy.Lorem ipsum dolor sit amet, in aecenas pharetra gravida ullamcorper neque. Sed hendrerit proin odio placerat ultrices adipiscing lectus ornare, ut velit nonummy.</p>

  <div class="estimate-tab">QUICK ESTIMATE</div>
  <aside class="info-panel">
    <h2 class="panel-heading">WE ARE</h2>
    <ul class="panel-list">
      <li>Locally Owned &amp; Operated</li>
      <li>Reliable &amp; Affordable</li>
      <li>All Supplies Provided</li>
      <li>Green Cleaning</li>
      <li>Pet Friendly</li>
      <li>No Contracts</li>
    </ul>
    <h2 class="panel-heading second">ON EVERY VISIT</h2>
    <ul class="panel-list visit-list">
      <li>We thoroughly clean your bathrooms, kitchen, bedrooms and living areas</li>
      <li>Mop or vacuum your floors</li>
      <li>Dust surfaces</li>
      <li>Collect garbage</li>
      <li>Make beds</li>
    </ul>
  </aside>

  <a class="job-link">Looking for a Job? &gt;&gt;</a>

  <section class="call-band">
    <span class="call-number">555-014-2290</span>
    <span class="call-prompt">Call Us Today!</span>
  </section>

  <nav class="main-nav">
    <a class="current" style="left:83px;width:116px;">about us</a>
    <a style="left:255px;width:125px;">our services</a>
    <a style="left:440px;width:85px;">reviews</a>
    <a style="left:590px;width:80px;">photos</a>
    <a style="left:740px;width:110px;">simple tips</a>
    <a style="left:910px;width:110px;">contact us</a>
    <a style="left:1085px;width:55px;">FAQ</a>
  </nav>
</body>
</html>
```